Flyer-Design für Wechseljahresberatung
Zielgruppe
Zielgruppe: überwiegend Frauen
psycholog. Beratung in allen Lebenslagen, Wechseljahresberatung , Gesundheits- und Ernährungsberatung, Fastenbegleitung, Trauerbegleitung, Bachblütenberatung,Klangmassagen
Aufgabenstellung
es geht um einen 6teiligen Kurs für Frauen zwischen Ende 30 bis Ende 60. Beginn der Wechseljahre , Leben in den Wechseljahren und was kommt danach? Wie erkennt man (Frau) körperl. oder seelische Probleme, die schon auf We.jahre hindeuten? Wie gehe Frau damit um? Was passiert in den We.jahren? Was kann Frau selbst tun, um die We.jahre so gut wie möglich zu erleben? Im Kurs werden natürliche Hilfsmittel besprochen und erklärt, Entspannungstechniken vermittelt , die Psyche gestärkt, sodaß die betroffenen Frauen bei auftretenden We.jahrsproblemen die Möglichkeit haben,sich selbst helfen zu können.

```html
<!DOCTYPE html>
<html lang="de">
<head>
<meta charset="utf-8">
<title>Selvara – Kurs Wechseljahre</title>
<link rel="stylesheet" href="https://fonts.googleapis.com/css2?family=Mulish:ital,wght@0,400;0,700;0,800;1,400&family=Yellowtail&display=swap">
<style>
  :root {
    --page-bg: #bdbdbd;
    --paper: #ffffff;
    --ink: #111111;
    --frame: #222222;
    --sky-top: #2f5d94;
    --sky-bottom: #6c93c2;
    --cloud: #f4f7fb;
    --hands-a: #8a6f63;
    --hands-b: #d9c3b4;
    --hands-c: #f1ebe6;
    --park-a: #6f8a4a;
    --park-b: #a9b98a;
    --park-c: #4e6a8e;
    --script-dark: #000000;
    --script-light: #ffffff;
  }
  * { margin: 0; padding: 0; box-sizing: border-box; }
  html, body {
    width: 1200px; height: 2728px; overflow: hidden;
    background: var(--page-bg);
  }
  .flyer {
    position: absolute; left: 81px; top: 125px;
    width: 1023px; height: 2490px;
    background: var(--paper);
    border: 2px solid var(--frame);
    overflow: hidden;
    font-family: "Mulish", "Avenir Next", sans-serif;
    color: var(--ink);
  }
  .sky-banner {
    position: absolute; left: 0; top: 0; width: 100%; height: 394px;
    background: linear-gradient(180deg, var(--sky-top), var(--sky-bottom));
  }
  .sky-title {
    position: absolute; left: 0; top: 120px; width: 100%;
    text-align: center; white-space: nowrap;
    font-family: "Mulish", "Avenir Next", sans-serif;
    font-style: italic; font-weight: 400;
    font-size: 172px; line-height: 1; letter-spacing: 2px;
    color: var(--cloud);
    text-shadow: 0 0 10px rgba(255,255,255,0.9), 0 0 22px rgba(255,255,255,0.6);
  }
  .hands-banner {
    position: absolute; left: 0; top: 394px; width: 100%; height: 423px;
    background: linear-gradient(110deg, var(--hands-a) 0%, var(--hands-b) 45%, var(--hands-c) 100%);
  }
  .script-title {
    position: absolute; left: 0; width: 100%;
    text-align: center; white-space: nowrap;
    font-family: "Yellowtail", cursive; font-weight: 400; line-height: 1;
  }
  .script-title--help { top: 125px; font-size: 110px; color: var(--script-dark); }
  .course-text {
    position: absolute; left: 60px; top: 860px; width: 920px;
    font-size: 37px; line-height: 54px;
  }
  .course-text .intro { margin-bottom: 28px; }
  .course-text strong { font-weight: 800; }
  .park-photo {
    position: absolute; left: 0; top: 1338px; width: 100%; height: 589px;
    background: linear-gradient(160deg, var(--park-b) 0%, var(--park-a) 55%, var(--park-c) 100%);
  }
  .script-title--interest { top: 245px; font-size: 108px; color: var(--script-light); }
  .contact {
    position: absolute; left: 60px; top: 1975px; width: 920px;
  }
  .contact-name { font-size: 46px; font-weight: 700; line-height: 62px; }
  .contact-lines { margin-top: 46px; font-size: 37px; line-height: 54px; }
  .contact-address { margin-top: 46px; font-size: 37px; line-height: 54px; }
  .brand-mark {
    position: absolute; left: 770px; top: 1995px; width: 200px;
    display: flex; flex-direction: column; align-items: center; gap: 14px;
  }
  .brand-mark svg { display: block; }
  .brand-mark .brand-name { font-size: 34px; font-weight: 700; letter-spacing: 4px; }
</style>
</head>
<body>
  <main class="flyer">
    <section class="sky-banner" role="img" aria-label="Blauer Himmel mit Wolken">
      <h1 class="sky-title">menopause</h1>
    </section>

    <section class="hands-banner" role="img" aria-label="Foto: zwei Hände halten einander tröstend">
      <h2 class="script-title script-title--help">Wir Helfen</h2>
    </section>

    <section class="course-text">
      <p class="intro">In einem <strong>6</strong> teiligen Kurs werden:</p>
      <p><strong>natürliche Hilfsmittel</strong>&nbsp; besprochen,<br>
      <strong>Entspannungstechniken</strong> vermittelt,<br>
      <strong>die Psyche gestärkt</strong>, sodaß die<br>
      betroffenen Frauen bei auftretenden<br>
      Wechseljahrsproblemen die Möglichkeit<br>
      haben, <strong>sich selbst helfen</strong> zu können.</p>
    </section>

    <section class="park-photo" role="img" aria-label="Foto: lächelnde Frau sitzt entspannt im Park zwischen Bäumen">
      <h2 class="script-title script-title--interest">Interesse Geweckt?</h2>
    </section>

    <section class="contact">
      <p class="contact-name">Selvara<br>Henrike Vosskamp-Lindner</p>
      <p class="contact-lines">Telefon: 0241/ 90 47 12 36<br>
      oder&nbsp; +31(0)45/ 7 12 38 64<br>
      mondhalmkreise@postfach-beispiel.de</p>
      <p class="contact-address">Adresse: Lindenhofweg 12, 6411AB Musterveld/NL</p>
    </section>

    <div class="brand-mark">
      <svg width="90" height="90" viewBox="0 0 90 90" aria-hidden="true">
        <circle cx="45" cy="45" r="40" fill="none" stroke="#111111" stroke-width="4"/>
      </svg>
      <span class="brand-name">SELVARA</span>
    </div>
  </main>
</body>
</html>
```